Word document template for sales proposals

I am after a template that is simple but impactful. Use of colour to be limited but some for impact would be good. The proposals are for use in the professional technical field.

```html
<!DOCTYPE html>
<html lang="en">
<head>
<meta charset="utf-8">
<title>Norvale — Proposal Template</title>
<link href="https://fonts.googleapis.com/css2?family=Montserrat:wght@300;400;500;600;700;800;900&display=swap" rel="stylesheet">
<style>
  :root{
    --orange:#f6921e;
    --blue:#29a9e0;
    --ink:#2b2b2b;
    --muted:#c9ccd3;
    --panel:#eef1f7;
    --panel-soft:#f4f6fa;
    --paper:#ffffff;
  }
  *{box-sizing:border-box;margin:0;padding:0}
  html,body{width:1200px;height:1200px;overflow:hidden}
  body{font-family:'Montserrat',sans-serif;color:var(--ink);background:var(--paper);position:relative}

  .brand-stage{position:absolute;left:0;top:0;width:1200px;height:378px;background:var(--paper)}
  .brand-dot{position:absolute;left:555px;top:95px;width:90px;height:90px;border-radius:50%;background:var(--blue)}
  .brand-name{position:absolute;left:0;top:238px;width:1200px;text-align:center;font-weight:800;font-size:60px;letter-spacing:2px;color:var(--orange);line-height:1}

  .showcase{position:absolute;left:0;top:378px;width:1200px;height:822px;background:var(--blue)}

  .page{position:absolute;height:293px;background:var(--paper);overflow:hidden;box-shadow:0 9px 10px -7px rgba(0,0,0,.35)}
  .row-1{top:491px}
  .row-2{top:812px}
  .fold-left::after{content:"";position:absolute;right:0;top:0;width:8px;height:100%;background:linear-gradient(90deg,rgba(0,0,0,0),rgba(0,0,0,.06))}
  .fold-right::before{content:"";position:absolute;left:0;top:0;width:6px;height:100%;background:linear-gradient(90deg,rgba(0,0,0,.07),rgba(0,0,0,0));z-index:3}
  .abs{position:absolute}

  .footer-brand{position:absolute;left:0;right:0;bottom:16px;text-align:center;font-weight:700;font-size:8px;letter-spacing:.5px;color:var(--orange)}
  .corner{position:absolute;top:0;width:23px;height:22px;background:var(--orange)}
  .corner.left{left:0}.corner.right{right:0}
  .page-title{position:absolute;left:0;right:0;text-align:center;font-weight:400;font-size:11px;letter-spacing:3px;color:var(--ink)}
  .label{font-size:7px;letter-spacing:1.4px;font-weight:500;color:var(--ink)}
  .faint{font-size:4.6px;line-height:1.35;color:var(--muted)}
  .tick-bar{position:absolute;left:0;width:4px;height:16px;background:var(--orange)}
  .placeholder{position:absolute;background:linear-gradient(135deg,#e9edf5,#f5f7fb)}

  /* cover */
  .cover-spine{position:absolute;left:12px;top:0;width:1px;height:100%;background:#e2e4ea}
  .cover-brand{position:absolute;left:0;right:0;top:44px;text-align:center;font-weight:700;font-size:9px;color:var(--orange)}
  .cover-kicker{position:absolute;left:80px;top:104px;font-weight:800;font-size:12.5px;letter-spacing:3px;color:var(--orange)}
  .cover-box{position:absolute;left:74px;top:121px;width:132px;height:94px;background:var(--orange);padding:8px 11px;color:#fff}
  .cover-box h1{font-weight:800;font-size:10.5px;letter-spacing:2.6px}
  .cover-box hr{border:0;height:1px;background:rgba(255,255,255,.8);width:84px;margin:5px 0 6px}
  .cover-box p{font-size:5px;line-height:1.3}

  /* about */
  .about-title{position:absolute;left:19px;top:63px;font-weight:300;font-size:15px;letter-spacing:4px;color:var(--orange)}
  .about-box{position:absolute;left:0;top:86px;width:149px;height:147px;background:var(--orange);padding:22px 12px 0;color:#fff}
  .about-box p{font-size:9.4px;line-height:1.18;font-weight:400}
  .about-sign{position:absolute;right:18px;bottom:17px;font-size:5px;letter-spacing:1px}

  /* contents */
  .content-tab{position:absolute;left:52px;top:0;width:106px;height:38px;background:var(--orange);color:#fff;font-size:11px;letter-spacing:3px;text-align:center;padding-top:9px}
  .toc-row{position:absolute;left:35px;width:165px}
  .toc-row .label{font-size:5.8px}
  .toc-row .faint{width:65px;margin-top:2px}
  .toc-dots{position:absolute;left:66px;top:4px;width:54px;border-bottom:1px dotted #777}
  .toc-num{position:absolute;left:128px;top:0;font-size:6.5px;letter-spacing:1px}

  /* process */
  .proc-item{position:absolute;left:24px;width:150px}
  .proc-item .num{font-weight:800;font-size:10px;color:var(--orange);letter-spacing:1px}
  .bar-row{position:absolute;left:10px;width:190px;height:12px}
  .bar-row .idx{position:absolute;left:0;top:0;font-weight:800;font-size:10px;letter-spacing:1.5px}
  .bar-row .track{position:absolute;left:27px;top:5px;width:126px;height:1px;background:#e4e6ec}
  .bar-row .fill{position:absolute;left:27px;top:4px;height:3px;border-radius:2px;background:var(--orange)}
  .bar-row .pct{position:absolute;left:160px;top:2px;font-weight:700;font-size:5.5px}

  /* structure */
  .icon-sq{position:absolute;width:22px;height:22px;background:var(--orange)}
  .icon-sq svg{width:22px;height:22px}
  .icon-label{position:absolute;font-weight:800;font-size:4.6px;letter-spacing:1px}

  .hist-note{position:absolute;width:80px;font-size:3.9px;line-height:1.3;color:#555;padding-left:4px}
  .hist-note::before{content:"";position:absolute;left:0;top:-3px;width:11px;height:10px;background:var(--orange);z-index:-1}
  .quote-text{position:absolute;font-size:6px;line-height:1.25;color:#444;width:98px}

  .big-num{position:absolute;font-weight:900;font-size:15px;letter-spacing:1px;color:var(--orange)}
  .big-note{position:absolute;font-size:4.2px;line-height:1.3;color:#444;width:118px}
</style>
</head>
<body>

<section class="brand-stage">
  <div class="brand-dot"></div>
  <div class="brand-name">NORVALE</div>
</section>

<section class="showcase"></section>

<!-- Cover -->
<article class="page row-1 cover" style="left:61px;width:206px">
  <div class="cover-spine"></div>
  <div class="cover-brand">NORVALE</div>
  <div class="placeholder" style="left:21px;top:53px;width:76px;height:212px" role="img" aria-label="Soft abstract background shapes"></div>
  <div class="placeholder" style="left:55px;top:63px;width:113px;height:173px;background:linear-gradient(135deg,#e4e8f0,#f1f3f8)" role="img" aria-label="Cover photograph area"></div>
  <div class="cover-kicker">PROPOSALS</div>
  <div class="cover-box">
    <h1>TEMPLATE</h1>
    <hr>
    <p>Lorem ipsum dolor sit amet, consectetuer adipiscing elit, sed diam</p>
  </div>
</article>

<!-- About -->
<article class="page row-1 fold-left" style="left:288px;width:199px">
  <div class="placeholder" style="left:109px;top:46px;width:77px;height:212px" role="img" aria-label="Soft abstract background shapes"></div>
  <div class="about-title">ABOUT</div>
  <div class="about-box">
    <p>Lorem ipsum dolor sit amet, consectetuer adipiscing elit, sed diam nonummy nibh euismod tincidunt ut laoreet dolore magna aliquam erat volutpat. Ut wisi enim ad</p>
    <div class="about-sign">LENA HART</div>
  </div>
  <div class="footer-brand">NORVALE</div>
</article>

<!-- Contents -->
<article class="page row-1 fold-right" style="left:487px;width:212px">
  <div class="content-tab">CONTENT</div>
  <div class="tick-bar" style="top:63px"></div>
  <div class="tick-bar" style="top:100px"></div>
  <div class="tick-bar" style="top:137px"></div>
  <div class="tick-bar" style="top:174px"></div>
  <div class="toc-row" style="top:64px"><div class="label">LOREM IPSUM</div><div class="faint">Brief summary of this section</div><div class="toc-dots"></div><div class="toc-num">01</div></div>
  <div class="toc-row" style="top:101px"><div class="label">LOREM IPSUM</div><div class="faint">Brief summary of this section</div><div class="toc-dots"></div><div class="toc-num">02</div></div>
  <div class="toc-row" style="top:138px"><div class="label">LOREM IPSUM</div><div class="faint">Brief summary of this section</div><div class="toc-dots"></div><div class="toc-num">03</div></div>
  <div class="toc-row" style="top:175px"><div class="label">LOREM IPSUM</div><div class="faint">Brief summary of this section</div><div class="toc-dots"></div><div class="toc-num">04</div></div>
  <div class="footer-brand">NORVALE</div>
</article>

<!-- Overview -->
<article class="page row-1 fold-left" style="left:727px;width:204px">
  <div class="corner left"></div>
  <div class="page-title" style="top:9px">OVERVIEW</div>
  <div class="tick-bar" style="top:57px;width:3px;height:18px"></div>
  <div class="tick-bar" style="top:86px;width:3px;height:18px"></div>
  <div class="abs" style="left:20px;top:54px;width:170px"><div class="label">LOREM IPSUM</div><div class="faint">Lorem ipsum dolor sit amet, consectetuer adipiscing elit, sed diam nonummy nibh euismod tincidunt ut laoreet dolore</div></div>
  <div class="abs" style="left:20px;top:83px;width:170px"><div class="label">LOREM IPSUM</div><div class="faint">Lorem ipsum dolor sit amet, consectetuer adipiscing elit, sed diam nonummy nibh euismod tincidunt ut laoreet dolore</div></div>
  <div class="placeholder" style="left:0;top:112px;width:204px;height:105px;background:#edf0f7" role="img" aria-label="Background image area"></div>
  <svg class="abs" style="left:0;top:112px" width="204" height="105" viewBox="0 0 204 105">
    <g font-family="Montserrat, sans-serif" text-anchor="middle">
      <text x="48" y="26" font-size="10" font-weight="800" letter-spacing="1.5">01</text>
      <text x="102" y="26" font-size="10" font-weight="800" letter-spacing="1.5">02</text>
      <text x="154" y="26" font-size="10" font-weight="800" letter-spacing="1.5">03</text>
      <circle cx="48" cy="59" r="20" fill="none" stroke="#555" stroke-width=".6"/>
      <circle cx="48" cy="59" r="20" fill="none" stroke="#f6921e" stroke-width="2.6" stroke-dasharray="88 38" transform="rotate(-120 48 59)"/>
      <circle cx="102" cy="59" r="20" fill="none" stroke="#555" stroke-width=".6"/>
      <circle cx="102" cy="59" r="20" fill="none" stroke="#fcd27a" stroke-width="2.6" stroke-dasharray="38 88" transform="rotate(40 102 59)"/>
      <circle cx="154" cy="59" r="20" fill="none" stroke="#555" stroke-width=".6"/>
      <circle cx="154" cy="59" r="20" fill="none" stroke="#f6921e" stroke-width="2.6" stroke-dasharray="20 43" transform="rotate(130 154 59)"/>
      <text x="48" y="61" font-size="5.5" font-weight="700">70%</text>
      <text x="102" y="61" font-size="5.5" font-weight="700">30%</text>
      <text x="154" y="61" font-size="5.5" font-weight="700">40%</text>
    </g>
  </svg>
  <div class="abs" style="left:19px;top:223px;width:78px;font-size:3.8px;line-height:1.3;color:#444">Lorem ipsum dolor sit amet, consectetuer adipiscing elit, sed diam nonummy nibh euismod tincidunt ut laoreet dolore</div>
  <div class="abs" style="left:114px;top:223px;width:78px;font-size:3.8px;line-height:1.3;color:#444">Lorem ipsum dolor sit amet, consectetuer adipiscing elit, sed diam nonummy nibh euismod tincidunt ut laoreet dolore</div>
  <div class="footer-brand">NORVALE</div>
</article>

<!-- Process -->
<article class="page row-1 fold-right" style="left:931px;width:206px">
  <div class="corner right"></div>
  <div class="page-title" style="top:9px">PROCESS</div>
  <div class="proc-item" style="top:41px"><div class="label">LOREM IPSUM <span class="num">01</span></div><div class="faint">Lorem ipsum dolor sit amet, consectetuer adipiscing elit, sed diam nonummy nibh euismod tincidunt ut laoreet dolore</div></div>
  <div class="proc-item" style="top:74px"><div class="label">LOREM IPSUM <span class="num">02</span></div><div class="faint">Lorem ipsum dolor sit amet, consectetuer adipiscing elit, sed diam nonummy nibh euismod tincidunt ut laoreet dolore</div></div>
  <div class="abs" style="left:0;right:0;top:124px;text-align:center;font-weight:700;font-size:6px">lorem ipsum</div>
  <div class="bar-row" style="top:138px"><span class="idx">01</span><span class="track"></span><span class="fill" style="width:34px"></span><span class="pct">20%</span></div>
  <div class="bar-row" style="top:157px"><span class="idx">02</span><span class="track"></span><span class="fill" style="width:91px"></span><span class="pct">80%</span></div>
  <div class="bar-row" style="top:175px"><span class="idx">03</span><span class="track"></span><span class="fill" style="width:68px"></span><span class="pct">70%</span></div>
  <div class="bar-row" style="top:192px"><span class="idx">04</span><span class="track"></span><span class="fill" style="width:14px"></span><span class="pct">10%</span></div>
  <div class="abs" style="left:24px;top:218px;width:140px;font-size:5.8px;line-height:1.2;color:#444">*Lorem ipsum dolor sit amet, consectetuer adipiscing elit, sed diam nonummy nibh</div>
  <div class="footer-brand">NORVALE</div>
</article>

<!-- Structure -->
<article class="page row-2 fold-left" style="left:58px;width:210px">
  <div class="corner left"></div>
  <div class="page-title" style="top:17px;font-size:11.5px">STRUCTURE</div>
  <div class="placeholder" style="left:194px;top:36px;width:16px;height:100px;background:#eef2fa"></div>
  <svg class="abs" style="left:0;top:0" width="210" height="120"><line x1="103" y1="42" x2="103" y2="118" stroke="#ccc" stroke-width=".5" stroke-dasharray="2 2"/><line x1="20" y1="80" x2="190" y2="80" stroke="#ccc" stroke-width=".5" stroke-dasharray="2 2"/></svg>
  <div class="icon-label" style="left:19px;top:59px">LOREM IPSUM</div>
  <div class="icon-label" style="left:144px;top:59px">LOREM IPSUM</div>
  <div class="icon-label" style="left:19px;top:92px">LOREM IPSUM</div>
  <div class="icon-label" style="left:144px;top:92px">LOREM IPSUM</div>
  <div class="icon-sq" style="left:70px;top:53px"><svg viewBox="0 0 22 22"><circle cx="11" cy="11" r="5" fill="none" stroke="#222" stroke-width="1"/><circle cx="11" cy="11" r="1.6" fill="#222"/></svg></div>
  <div class="icon-sq" style="left:113px;top:53px"><svg viewBox="0 0 22 22"><circle cx="11" cy="7.5" r="2.4" fill="none" stroke="#222" stroke-width="1"/><path d="M6.5 17v-3a4.5 4.5 0 0 1 9 0v3z" fill="none" stroke="#222" stroke-width="1"/></svg></div>
  <div class="icon-sq" style="left:70px;top:86px"><svg viewBox="0 0 22 22"><path d="M4 10l7-3 7 3-7 3z M7.5 11.5v3.5c2 1.5 5 1.5 7 0v-3.5" fill="none" stroke="#222" stroke-width="1"/></svg></div>
  <div class="icon-sq" style="left:113px;top:86px"><svg viewBox="0 0 22 22"><path d="M7 17V5 M7 6h9l-2 3 2 3H7" fill="none" stroke="#222" stroke-width="1"/></svg></div>
  <div class="tick-bar" style="top:143px"></div>
  <div class="tick-bar" style="top:187px"></div>
  <div class="tick-bar" style="top:232px"></div>
  <div class="abs" style="left:13px;top:137px;width:115px"><div class="label">LOREM IPSUM</div><div class="faint">Lorem ipsum dolor sit amet, consectetuer adipiscing elit, sed diam nonummy nibh euismod tincidunt ut laoreet dolore</div></div>
  <div class="abs" style="left:13px;top:182px;width:115px"><div class="label">LOREM IPSUM</div><div class="faint">Lorem ipsum dolor sit amet, consectetuer adipiscing elit, sed diam nonummy nibh euismod tincidunt ut laoreet dolore</div></div>
  <div class="abs" style="left:13px;top:226px;width:115px"><div class="label">LOREM IPSUM</div><div class="faint">Lorem ipsum dolor sit amet, consectetuer adipiscing elit, sed diam nonummy nibh euismod tincidunt ut laoreet dolore</div></div>
  <div class="placeholder" style="left:130px;top:173px;width:80px;height:120px;background:#e8ebf2" role="img" aria-label="Team photograph area"></div>
  <div class="abs" style="left:130px;top:209px;width:80px;text-align:center;font-weight:800;font-size:7.5px;letter-spacing:1.6px;line-height:1.25">LOREM<br>IPSUM</div>
  <div class="footer-brand">NORVALE</div>
</article>

<!-- History -->
<article class="page row-2 fold-right" style="left:268px;width:201px">
  <div class="corner right"></div>
  <div class="page-title" style="top:8px">HISTORY</div>
  <div class="placeholder" style="left:0;top:36px;width:201px;height:100px;background:#eef2fa"></div>
  <div class="hist-note" style="left:12px;top:56px">Lorem ipsum dolor sit amet, consectetuer adipiscing elit, sed diam nonummy nibh euismod tincidunt ut laoreet dolore</div>
  <div class="hist-note" style="left:107px;top:56px">Lorem ipsum dolor sit amet, consectetuer adipiscing elit, sed diam nonummy nibh euismod tincidunt ut laoreet dolore</div>
  <div class="hist-note" style="left:12px;top:93px">Lorem ipsum dolor sit amet, consectetuer adipiscing elit, sed diam nonummy nibh euismod tincidunt ut laoreet dolore</div>
  <div class="hist-note" style="left:107px;top:93px">Lorem ipsum dolor sit amet, consectetuer adipiscing elit, sed diam nonummy nibh euismod tincidunt ut laoreet dolore</div>
  <div class="abs" style="left:0;right:0;top:148px;text-align:center;font-size:11px;color:var(--orange)">LOREM IPSUM</div>
  <div class="placeholder" style="left:0;top:173px;width:74px;height:120px;background:#e8ebf2" role="img" aria-label="Image area"></div>
  <div class="abs" style="left:0;top:185px;width:74px;text-align:center;font-size:7px;letter-spacing:1.8px;line-height:1.2">“LOREM IPSUM DOLOR SIT AMET, CON-SECTE-</div>
  <svg class="abs" style="left:80px;top:186px" width="12" height="55" viewBox="0 0 12 55">
    <circle cx="6" cy="3" r="2.4" fill="none" stroke="#f6921e" stroke-width=".8"/><path d="M1.5 12v-3a4.5 4.5 0 0 1 9 0v3z" fill="none" stroke="#f6921e" stroke-width=".8"/>
    <circle cx="6" cy="47" r="4" fill="none" stroke="#f6921e" stroke-width=".8"/><circle cx="6" cy="47" r="1.5" fill="none" stroke="#f6921e" stroke-width=".8"/>
  </svg>
  <div class="quote-text" style="left:97px;top:186px">*Lorem ipsum dolor sit amet, consectetuer adipiscing elit, sed diam nonummy nibh</div>
  <div class="quote-text" style="left:97px;top:225px">*Lorem ipsum dolor sit amet, consectetuer adipiscing elit, sed diam nonummy nibh</div>
  <div class="footer-brand">NORVALE</div>
</article>

<!-- Values -->
<article class="page row-2 fold-left" style="left:492px;width:208px">
  <div class="corner left"></div>
  <div class="page-title" style="top:8px">VALUES</div>
  <svg class="abs" style="left:0;top:36px" width="208" height="150" viewBox="0 36 208 150">
    <g fill="none">
      <circle cx="69" cy="72" r="28" stroke="#999" stroke-width=".5" stroke-dasharray="1 1.5"/>
      <circle cx="69" cy="72" r="28" stroke="#f6921e" stroke-width="4" stroke-linecap="round" stroke-dasharray="135 41" transform="rotate(-90 69 72)"/>
      <circle cx="140" cy="72" r="28" stroke="#999" stroke-width=".5" stroke-dasharray="1 1.5"/>
      <circle cx="140" cy="72" r="28" stroke="#f6921e" stroke-width="4" stroke-linecap="round" stroke-dasharray="110 66" transform="rotate(0 140 72)"/>
      <circle cx="68" cy="143" r="28" stroke="#999" stroke-width=".5" stroke-dasharray="1 1.5"/>
      <circle cx="68" cy="143" r="28" stroke="#f6921e" stroke-width="4" stroke-linecap="round" stroke-dasharray="100 76" transform="rotate(95 68 143)"/>
      <circle cx="140" cy="143" r="28" stroke="#999" stroke-width=".5" stroke-dasharray="1 1.5"/>
      <circle cx="140" cy="143" r="28" stroke="#f6921e" stroke-width="4" stroke-linecap="round" stroke-dasharray="90 86" transform="rotate(20 140 143)"/>
      <path d="M93 46q12-6 24 0 M113 43l4 3-4 3" stroke="#bbb" stroke-width="1"/>
      <path d="M171 86q6 12 0 24 M168 107l3 4 3-4" stroke="#bbb" stroke-width="1"/>
      <path d="M117 170q-12 6-24 0 M97 173l-4-3 4-3" stroke="#bbb" stroke-width="1"/>
      <path d="M37 128q-6-12 0-24 M34 108l3-4 3 4" stroke="#bbb" stroke-width="1"/>
    </g>
    <g font-family="Montserrat, sans-serif" text-anchor="middle" fill="#222">
      <text x="69" y="69" font-size="4.5" font-weight="700">12</text>
      <text x="69" y="75" font-size="2.6">Key value note</text>
      <text x="140" y="69" font-size="4.5" font-weight="700">37</text>
      <text x="140" y="75" font-size="2.6">Key value note</text>
      <text x="68" y="140" font-size="4.5" font-weight="700">15</text>
      <text x="68" y="146" font-size="2.6">Key value note</text>
      <text x="140" y="140" font-size="4.5" font-weight="700">35</text>
      <text x="140" y="146" font-size="2.6">Key value note</text>
    </g>
  </svg>
  <div class="big-num" style="left:37px;top:189px">01</div>
  <div class="big-note" style="left:58px;top:193px">Lorem ipsum dolor sit amet, consectetuer adipiscing elit, sed diam nonummy nibh euismod tincidunt ut laoreet dolore</div>
  <div class="big-num" style="left:37px;top:221px">02</div>
  <div class="big-note" style="left:58px;top:224px">Lorem ipsum dolor sit amet, consectetuer adipiscing elit, sed diam nonummy nibh euismod tincidunt ut laoreet dolore</div>
  <div class="footer-brand">NORVALE</div>
</article>

<!-- Future -->
<article class="page row-2 fold-right" style="left:700px;width:203px">
  <div class="corner right"></div>
  <div class="page-title" style="top:8px">FUTURE</div>
  <div class="faint abs" style="left:23px;top:30px;width:155px">Lorem ipsum dolor sit amet, consectetuer adipiscing elit, sed diam nonummy nibh euismod tincidunt ut laoreet dolore</div>
  <div class="placeholder" style="left:0;top:60px;width:181px;height:108px;background:#e6eaf3" role="img" aria-label="Outlook photograph area"></div>
  <div class="abs" style="left:23px;top:178px;width:155px"><div class="label">LOREM IPSUM</div><div class="faint" style="margin-top:3px">Lorem ipsum dolor sit amet, consectetuer adipiscing elit, sed diam nonummy nibh euismod tincidunt ut laoreet dolore</div></div>
  <div class="abs" style="left:23px;top:220px;width:155px"><div class="label">LOREM IPSUM</div><div class="faint" style="margin-top:3px">Lorem ipsum dolor sit amet, consectetuer adipiscing elit, sed diam nonummy nibh euismod tincidunt ut laoreet dolore</div></div>
  <div class="footer-brand">NORVALE</div>
</article>

<!-- Back cover -->
<article class="page row-2" style="left:931px;width:206px">
  <div class="cover-spine"></div>
  <div class="placeholder" style="left:0;top:141px;width:206px;height:55px;background:var(--panel-soft)" role="img" aria-label="Soft abstract background shapes"></div>
  <div class="placeholder" style="left:23px;top:85px;width:158px;height:99px;background:#e8ebf2" role="img" aria-label="Image area"></div>
  <div class="abs" style="left:36px;top:90px;width:132px;height:93px;background:var(--orange);color:#fff;text-align:center;padding-top:34px">
    <div style="font-weight:700;font-size:8px">NORVALE</div>
    <div style="height:1px;background:rgba(255,255,255,.8);width:76px;margin:5px auto 6px"></div>
    <div style="font-size:5px;line-height:1.3;padding:0 10px">Lorem ipsum dolor sit amet, consectetuer adipiscing elit, sed diam</div>
  </div>
</article>

</body>
</html>
```